Flyer design for our aerial photography service

We need an 8.5x11 two sided design flyer that will showcase our aerial photography service. No pricing or text is needed aside from our logo and somewhere on the page the title "Aerial Photography". I would like it be a black background with our logo in white which I have attached. Please make it a creative stylish design that highlights the photos. Our Logo should be at the top. The logo should not be large and shouldnt be the focus of the page but should be fairly visible. I'm open to it being in different locations as well.

Industry/Entity Type

Real Estate

Font styles to use
Serif

Requirements
Must have
• Logo and photos and the title Aerial Photography
Nice to have
Should not have
• n/a

```html
<!DOCTYPE html>
<html lang="en">
<head>
<meta charset="utf-8">
<title>Aerial Photography Flyer</title>
<link rel="stylesheet" href="https://fonts.googleapis.com/css2?family=Oranienbaum&display=swap">
<style>
  :root {
    --canvas-bg: #e9e9ea;
    --flyer-black: #0c0c0c;
    --flyer-black-soft: #161616;
    --band-black: #030303;
    --title-silver: #7d858b;
    --title-highlight: #b9c0c5;
    --title-shade: #000000;
    --photo-border: #f2f2f0;
    --logo-white: #ffffff;
  }
  * { box-sizing: border-box; margin: 0; padding: 0; }
  html, body { width: 1200px; height: 1000px; overflow: hidden; }
  body {
    background: var(--canvas-bg);
    font-family: "Oranienbaum", "Times New Roman", serif;
    position: relative;
  }
  .flyer {
    position: absolute;
    top: 163px;
    width: 520px;
    height: 673px;
    overflow: hidden;
    background: linear-gradient(160deg, var(--flyer-black-soft), var(--flyer-black) 60%);
    box-shadow: 0 6px 18px rgba(0,0,0,0.25);
  }
  .flyer--front { left: 50px; }
  .flyer--back { left: 630px; }

  .flyer__title {
    position: absolute;
    top: 52px;
    left: 0;
    width: 100%;
    text-align: center;
    font-size: 50px;
    letter-spacing: 1px;
    color: var(--title-silver);
    text-shadow: -1px -1px 0 var(--title-highlight), 2px 2px 2px var(--title-shade);
    transform: scaleY(1.15);
  }
  .flyer__rule {
    position: absolute;
    top: 122px;
    left: 120px;
    width: 280px;
    height: 1px;
    background: var(--title-silver);
    opacity: 0.8;
  }

  .collage { position: absolute; inset: 0; }
  .photo {
    position: absolute;
    border: 6px solid var(--photo-border);
    box-shadow: 2px 4px 10px rgba(0,0,0,0.7);
  }
  .photo--lake   { background: linear-gradient(180deg, #5c8fcf 0%, #9fb8c9 25%, #4d7a3a 45%, #2f5b4f 100%); }
  .photo--pool   { background: linear-gradient(150deg, #b8642e 0%, #6f7d4a 35%, #8a8f95 55%, #3c8fc1 80%, #4a6e35 100%); }
  .photo--dusk   { background: linear-gradient(180deg, #7fa2b5 0%, #a0704a 35%, #c8b07a 50%, #4d7d2e 70%, #3b6a22 100%); }
  .photo--autumn { background: linear-gradient(160deg, #8fb1d6 0%, #b26a3a 30%, #7a7c80 55%, #3d3f44 100%); }
  .photo--garden { background: linear-gradient(170deg, #2d5a2a 0%, #3f7a3a 40%, #2a4a3c 70%, #5b7a4a 100%); }
  .photo--ridge  { background: linear-gradient(180deg, #c5ced4 0%, #7d8f6a 35%, #9fa3a6 55%, #3f6a34 100%); }
  .photo--roof   { background: linear-gradient(160deg, #3f6b36 0%, #6f7885 40%, #2d8fb5 65%, #4a7a33 100%); }
  .photo--deck   { background: linear-gradient(180deg, #bcd0e2 0%, #e8e8e4 35%, #6a7a5a 60%, #3f7030 100%); }
  .photo--lawn   { background: linear-gradient(170deg, #5b8fd0 0%, #c88a4a 30%, #bfc3c6 50%, #4f8a2f 100%); }
  .photo--cove   { background: linear-gradient(180deg, #c9d7e4 0%, #3f6e8a 35%, #5d6266 55%, #4c5a3e 100%); }

  .flyer__band {
    position: absolute;
    left: 0;
    bottom: 0;
    width: 100%;
    height: 110px;
    background: var(--band-black);
  }
  .brand {
    position: absolute;
    left: 0;
    bottom: 28px;
    width: 100%;
    text-align: center;
    color: var(--logo-white);
  }
  .brand__mark {
    display: block;
    width: 36px;
    height: 36px;
    margin: 0 auto 6px;
    border-radius: 50%;
    background: var(--logo-white);
  }
  .brand__name {
    display: block;
    font-size: 17px;
    line-height: 1.1;
    letter-spacing: 0.5px;
  }
  .brand__sub {
    display: block;
    font-size: 7px;
    letter-spacing: 3px;
    margin-top: 2px;
  }
</style>
</head>
<body>

<section class="flyer flyer--front">
  <h1 class="flyer__title">Aerial Photography</h1>
  <div class="flyer__rule"></div>
  <div class="collage">
    <div class="photo photo--lake" style="left:-6px;top:198px;width:188px;height:160px;transform:rotate(-3deg);" role="img" aria-label="Aerial photo of a lakeside home with a boat dock"></div>
    <div class="photo photo--pool" style="left:160px;top:192px;width:200px;height:168px;transform:rotate(-5deg);" role="img" aria-label="Aerial photo of a large home with a pool and deck among autumn trees"></div>
    <div class="photo photo--dusk" style="left:345px;top:196px;width:188px;height:150px;transform:rotate(-2deg);" role="img" aria-label="Photo of a lit two-storey house at dusk with a green lawn"></div>
    <div class="photo photo--autumn" style="left:70px;top:345px;width:198px;height:150px;transform:rotate(1.5deg);" role="img" aria-label="Aerial photo of a house with a garage and driveway in autumn"></div>
    <div class="photo photo--garden" style="left:250px;top:330px;width:205px;height:150px;transform:rotate(-3.5deg);" role="img" aria-label="Aerial photo of a house surrounded by gardens and trees"></div>
  </div>
  <div class="flyer__band"></div>
  <div class="brand">
    <span class="brand__mark"></span>
    <span class="brand__name">Skyward Lens</span>
    <span class="brand__sub">PHOTOGRAPHY</span>
  </div>
</section>

<section class="flyer flyer--back">
  <h1 class="flyer__title">Aerial Photography</h1>
  <div class="flyer__rule"></div>
  <div class="collage">
    <div class="photo photo--ridge" style="left:-6px;top:200px;width:190px;height:150px;transform:rotate(-1deg);" role="img" aria-label="Aerial photo of a hillside home among evergreen trees"></div>
    <div class="photo photo--roof" style="left:165px;top:200px;width:190px;height:160px;transform:rotate(-2deg);" role="img" aria-label="Aerial photo of a grey-roofed house with a curved swimming pool"></div>
    <div class="photo photo--deck" style="left:335px;top:212px;width:190px;height:165px;transform:rotate(3deg);" role="img" aria-label="Aerial photo of a white house with a deck and landscaped garden"></div>
    <div class="photo photo--lawn" style="left:40px;top:340px;width:195px;height:155px;transform:rotate(4deg);" role="img" aria-label="Aerial photo of a ranch house with a front lawn and brick walkway"></div>
    <div class="photo photo--cove" style="left:230px;top:348px;width:195px;height:150px;transform:rotate(-2deg);" role="img" aria-label="Aerial photo of a lakefront house with a garage and driveway"></div>
  </div>
  <div class="flyer__band"></div>
  <div class="brand">
    <span class="brand__mark"></span>
    <span class="brand__name">Skyward Lens</span>
    <span class="brand__sub">PHOTOGRAPHY</span>
  </div>
</section>

</body>
</html>
```